Private London College Prospectus

A single spread to begin with followed by treatments for a couple of awkward spreads in the brochure. Attached docs include previous few years to show how the design has evolved. We're now looking for a different direction
Outline: Private college in Central London.
Mainly A-levels but also GCSE courses
Consistently at the top of London results table
Operated by the owners
Prospectus is sent to anyone enquiring about the college

Target Market(s)

High net worth families in the Uk and abroad

Industry/Entity Type

College

Requirements
Must have
• Modern fonts
• House colour is purple - PMS 8804
• Teacher quote
• Page quote
Nice to have
• See attachments - the gryphon is part of their logo but not essential
Should not have
• Shouldn't be too fussy or cluttered
• No script fonts (probably) no italics in main text

```html
<!DOCTYPE html>
<html lang="en">
<head>
<meta charset="utf-8">
<title>Ashcombe College Prospectus – Spread 02–03</title>
<link href="https://fonts.googleapis.com/css2?family=Lato:ital,wght@0,400;0,700;0,900;1,700&family=Quicksand:wght@300;400&display=swap" rel="stylesheet">
<style>
  :root{
    --backdrop:#d9d8d4;
    --house-purple:#4b1f50;
    --house-purple-deep:#351538;
    --house-purple-glow:#64306a;
    --accent-plum:#7d2f6f;
    --folio-plum:#6a2a63;
    --paper:#ffffff;
    --paper-shade:#f1f0ee;
    --ink:#3a2a3c;
    --ink-soft:#6b6270;
    --on-purple:#eadfeb;
    --on-purple-soft:#c7b3c9;
    --photo-tone-a:#d8d6d2;
    --photo-tone-b:#b9b4ae;
  }
  *{box-sizing:border-box;margin:0;padding:0}
  html,body{width:1200px;height:804px;overflow:hidden}
  body{background:var(--backdrop);font-family:"Lato",sans-serif;position:relative}

  .spread{position:absolute;left:70px;top:22px;width:1060px;height:760px;display:flex;box-shadow:0 8px 30px rgba(0,0,0,.18)}
  .page{position:relative;width:530px;height:760px;overflow:hidden}

  /* Left page */
  .page--contents{background:radial-gradient(ellipse 75% 55% at 55% 30%,var(--house-purple-glow) 0%,var(--house-purple) 55%,var(--house-purple-deep) 100%);color:var(--on-purple)}
  .section-bar{position:absolute;left:0;top:218px;width:118px;height:24px;background:var(--accent-plum)}
  .contents-title{position:absolute;left:128px;top:206px;font-family:"Quicksand",sans-serif;font-weight:400;font-size:27px;color:#fff;letter-spacing:.2px}
  .contents-list{position:absolute;left:128px;top:252px;list-style:none;font-size:10.5px;line-height:14.4px}
  .contents-list li{display:flex}
  .contents-list .num{width:26px;color:var(--on-purple-soft)}
  .page-quote{position:absolute;right:110px;top:592px;text-align:right;font-size:9.5px;line-height:17px;color:var(--on-purple)}
  .page-quote q{font-style:italic;font-weight:700}
  .page-quote cite{display:block;font-style:normal;font-weight:700}
  .college-name{font-family:"Lato",sans-serif;font-weight:400;font-size:12px;display:flex;align-items:center;gap:6px}
  .college-name .mark{width:8px;height:8px;border-radius:50%}
  .page--contents .college-name{position:absolute;right:32px;top:664px;color:#fff}
  .page--contents .college-name .mark{background:var(--on-purple)}
  .footer-rule{position:absolute;height:1px}
  .page--contents .footer-rule{left:80px;right:30px;top:700px;background:rgba(255,255,255,.35)}
  .folio{position:absolute;bottom:0;width:30px;height:24px;background:var(--folio-plum);color:#fff;font-size:9.5px;display:flex;align-items:center;justify-content:center}
  .page--contents .folio{left:0}
  .contact-line{position:absolute;bottom:6px;font-size:9.5px}
  .page--contents .contact-line{left:42px;color:var(--on-purple)}

  /* Right page */
  .page--director{background:linear-gradient(90deg,var(--paper-shade) 0%,var(--paper) 8%,var(--paper) 100%);color:var(--ink)}
  .director-photo{position:absolute;left:258px;top:70px;width:204px;height:196px;background:linear-gradient(150deg,var(--photo-tone-a),var(--photo-tone-b))}
  .title-block{position:absolute;left:14px;top:186px;width:46px;height:46px;background:var(--house-purple)}
  .message-title{position:absolute;left:70px;top:166px;font-family:"Quicksand",sans-serif;font-weight:400;line-height:1.05}
  .message-title .lead{display:block;font-size:19px;color:var(--house-purple)}
  .message-title .role{display:block;font-size:24px;color:var(--ink-soft);text-transform:uppercase;font-weight:300}

  .message-copy{position:absolute;left:70px;top:242px;width:420px;display:flex;flex-direction:column;font-size:8.6px;line-height:12px}
  .message-copy .intro{width:178px;margin-bottom:16px}
  .message-copy .message-body p{margin-bottom:12px}
  .message-copy .message-body p:last-child{margin-bottom:0}
  .signature{width:64px;height:40px;margin:18px 0 8px 12px;background:linear-gradient(120deg,#e8e4ea,#f6f4f7)}
  .signatory .name{font-size:12px;line-height:15px;font-weight:900;color:var(--house-purple);text-transform:uppercase}
  .signatory .post{font-size:10px;line-height:13px;color:var(--ink)}

  .page--director .college-name{position:absolute;left:22px;top:720px;color:var(--house-purple)}
  .page--director .college-name .mark{background:var(--house-purple)}
  .page--director .footer-rule{left:130px;right:30px;top:728px;background:#cfc8d1}
  .page--director .contact-line{right:40px;color:var(--ink-soft)}
  .page--director .folio{right:0}
</style>
</head>
<body>
<main class="spread">
  <section class="page page--contents">
    <div class="section-bar"></div>
    <h1 class="contents-title">Content</h1>
    <ol class="contents-list">
      <li><span class="num">03</span>Lorem ipsum dolor sit amet tellus inter</li>
      <li><span class="num">04</span>consectetur adipiscing elit</li>
      <li><span class="num">05</span>Mauris ac dui nibh condimentum metus</li>
      <li><span class="num">06</span>Mauris ante tortor adipiscing at porta</li>
      <li><span class="num">07</span>commodo vel ipsum</li>
      <li><span class="num">08</span>Nam elementum tellus interdum</li>
      <li><span class="num">09</span>consectetur vene natis diam quam eleifend</li>
      <li><span class="num">10</span>sit amet pulvinar lectus erat a nibh</li>
      <li><span class="num">11</span>Suspendisse potenti</li>
      <li><span class="num">12</span>Cum sociis natoque penatibus et</li>
      <li><span class="num">13</span>magnis dis parturient montes</li>
      <li><span class="num">14</span>nascetur ridiculus mus</li>
      <li><span class="num">15</span>Donec laoreet lacinia mi ac aliquam</li>
      <li><span class="num">16</span>Nam sed urna sapien quis dictum nisl</li>
      <li><span class="num">17</span>consectetur adipiscing elit</li>
      <li><span class="num">18</span>Mauris ac dui nibh condimentum metus</li>
      <li><span class="num">19</span>Mauris ante tortor adipiscing at porta</li>
      <li><span class="num">20</span>commodo vel ipsum</li>
      <li><span class="num">21</span>Nam elementum tellus interdum</li>
      <li><span class="num">22</span>consectetur vene natis diam quam eleifend</li>
      <li><span class="num">23</span>sit amet pulvinar lectus erat a nibh</li>
      <li><span class="num">24</span>Suspendisse potenti</li>
    </ol>
    <blockquote class="page-quote">
      <q>The Quality of the Curriculum, Teaching and Learners’ Achievements is EXCELLENT</q>
      <cite>SRB INSPECTION REPORT - March 2016</cite>
    </blockquote>
    <div class="college-name"><span class="mark"></span>Ashcombe</div>
    <div class="footer-rule"></div>
    <div class="folio">02</div>
    <p class="contact-line">www.ashcombe.org.uk | admin@ashcombe.org.uk | (+44) 20 7946 0318</p>
  </section>

  <section class="page page--director">
    <div class="director-photo" role="img" aria-label="Portrait photograph of the director in a white shirt against a pale curtain"></div>
    <div class="title-block"></div>
    <h2 class="message-title"><span class="lead">Message from the</span><span class="role">Director</span></h2>
    <article class="message-copy">
      <p class="intro">Lorem ipsum dolor sit amet, consectetur adipiscing elit. Mauris ac dui nibh, a condimentum metus. Mauris ante tortor, adipiscing at porta tempus, commodo vel ipsum. Nam elementum, tellus interdum consectetur vene natis diam quam eleifend risus, sit amet pulvinar lectus erat a nibh. Suspendisse potenti.</p>
      <div class="message-body">
        <p>Cum sociis natoque penatibus et magnis dis parturient montes, nascetur ridiculus mus. Donec laoreet lacinia mi ac aliquam. Nam sed urna sapien, quis dictum nisl. Aliquam neque libero, sollicitudin vel iaculis nec, laoreet ut tortor. Duis convallis ullamcorper dui vel tempor. Donec scelerisque blandit lorem at bibendum.</p>
        <p>Nam a blandit purus. Fusce vel enim ipsum, non adipiscing justo. Vivamus dui libero, fermentum non imperdiet nec, vulputate placerat urna. Nullam arcu dui, egestas sit amet blandit nec, congue vel ipsum. Integer semper risus ac odio porta at sollicitudin diam elementum.</p>
        <p>Quisque rhoncus, mi ut vulputate rutrum, est diam condimentum turpis, iaculis rhoncus arcu felis sit amet nunc. Aliquam quis libero adipiscing tellus egestas faucibus nec at ipsum. Integer a ipsum elit. Fusce vestibulum pellentesque tellus eu hendrerit. Vestibulum ante ipsum primis in faucibus orci luctus et ultrices posuere cubilia Curae; Nam ut metus nec sapien cursus molestie.</p>
        <p>Nam a blandit purus. Fusce vel enim ipsum, non adipiscing justo. Vivamus dui libero, fermentum non imperdiet nec, vulputate placerat urna. Nullam arcu dui, egestas sit amet blandit nec, congue vel ipsum. Integer semper risus ac odio porta at sollicitudin diam elementum.</p>
      </div>
      <div class="signature" role="img" aria-label="Handwritten signature of the director"></div>
      <div class="signatory">
        <p class="name">Rohan Mehta</p>
        <p class="post">Head of Economics</p>
      </div>
    </article>
    <div class="college-name"><span class="mark"></span>Ashcombe</div>
    <div class="footer-rule"></div>
    <p class="contact-line">www.ashcombe.org.uk | admin@ashcombe.org.uk | (+44) 20 7946 0318</p>
    <div class="folio">03</div>
  </section>
</main>
</body>
</html>
```